Redesigning a sales pitch ppt document

This document is to be used as a sales-pitch - for an initial meeting with prospective clients.

Challenge is the document is rather boring graphically - formatting is in business consulting style, versus a more interesting sales brochure.

We will like to change the document to be much more fun, while being classic given that we are in the busines of selling experiential gifts. We will like to portray an image of a company that is fun, pioneering (we are one of the few companies doing experiential gifts in China), but at the same time, being very tasteful.

There are some Chinese words in the document but feel free to ignore as it should not impat the storyline.

What we are looking for:
- Re-do the ppt so it can have a new look and feel that portrays the above
- Have a ppt template for future documents

Note:
- We like the feel of the cover page - so we keep it in its current form though of course, happy to change fonts etc.
- All the other pages we can change.

Have attached the following:

1. current version of the file translated into English.
2. What some of the competitors do (the Lumo-Tine file) - but believe that this is too flashy and we are looking for something more tasteful and classy (though still have to be portrayed as cool and pioneering

For more information about the parent company (this business is a standalone subsidiary), you can visit www.farbrookvale.com and www.tarimov.com

Target Market(s)

China, Corporates - mostly in professional service and tech sector

Industry/Entity Type

Sales

Requirements
Must have
• Revised PPT with updated format
• Revised template
Nice to have
• Should be cool, pioneering while also showing the classy, heritage look as our gifts are classy but the idea of giving experiential gifts is pioneering (at least in China)
Should not have
• Am open to other fonts except for Sans Seirf

```html
<!DOCTYPE html>
<html lang="en">
<head>
<meta charset="utf-8">
<title>Wayfarel.gift — Sales Pitch Deck</title>
<link rel="stylesheet" href="https://fonts.googleapis.com/css2?family=Lato:wght@400;700;900&family=Noto+Sans+SC:wght@400;500&display=swap">
<style>
  :root{
    --canvas:#c6c7c9;
    --white:#ffffff;
    --ink:#2b3440;
    --muted:#55606b;
    --navy:#1b3a55;
    --navy-deep:#122a40;
    --brand-blue:#1669a3;
    --teal-link:#1b7fa6;
    --agenda-1:#0f5a8a;
    --agenda-2:#127f8c;
    --agenda-3:#18a88c;
    --accent-cyan:#29b3e8;
    --price-red:#d2232a;
  }
  *{box-sizing:border-box;margin:0;padding:0}
  html,body{width:836px;height:1200px;overflow:hidden}
  body{background:var(--canvas);font-family:"Lato","Noto Sans SC",sans-serif;color:var(--ink)}
  .deck{
    position:relative;width:836px;height:1200px;
    display:grid;grid-template-columns:396px 396px;grid-template-rows:repeat(5,222px);
    column-gap:9px;row-gap:9px;padding:32px 17px 0 18px;
  }
  .slide{position:relative;overflow:hidden;background:var(--white)}
  .photo{position:absolute;inset:0}

  /* Cover */
  .cover .photo{background:linear-gradient(160deg,#3b6f78 0%,#8e9a3e 30%,#c9b540 45%,#4f6a55 62%,#2a2a2a 100%)}
  .cover .brand-tab{position:absolute;left:114px;top:0;width:168px;height:48px;background:var(--white);border-radius:0 0 8px 8px;text-align:center;padding-top:6px}
  .brand-name{font-weight:900;font-size:18px;color:var(--brand-blue);letter-spacing:.5px}
  .brand-name small{font-weight:700;font-size:12px}
  .brand-tagline{font-family:"Noto Sans SC",sans-serif;font-size:9px;color:var(--teal-link);margin-top:1px}
  .cover .pitch-box{position:absolute;left:114px;top:58px;width:168px;height:68px;border:1.5px solid #3fb8c8;color:var(--white);font-family:"Noto Sans SC",sans-serif;font-size:9px;line-height:16px;text-align:center;padding-top:9px}
  .cover .footer{position:absolute;left:0;right:0;bottom:0;height:36px;background:var(--white);display:flex;align-items:center}
  .cover .mark{width:36px;height:36px;background:var(--brand-blue);display:flex;align-items:center;justify-content:center;margin-left:12px;margin-top:-10px;color:var(--white);font-size:5px;font-weight:700}
  .cover .disclaimer{font-size:5.6px;line-height:7.5px;color:var(--ink);margin-left:21px;width:310px}

  /* Agenda */
  .agenda .photo{height:124px;background:linear-gradient(180deg,#1a2632 0%,#2d3b48 60%,#243442 100%)}
  .agenda h2{position:absolute;top:28px;left:0;right:0;text-align:center;color:var(--white);font-weight:700;font-size:33px;letter-spacing:.5px}
  .agenda-item{position:absolute;top:92px;width:110px;text-align:center}
  .agenda-item .num{width:66px;height:66px;border-radius:50%;margin:0 auto;color:var(--white);font-size:30px;font-weight:700;display:flex;align-items:center;justify-content:center;box-shadow:0 3px 5px rgba(0,0,0,.3)}
  .agenda-item p{font-size:7px;color:var(--ink);margin-top:8px}

  /* Section dividers */
  .section .photo-products{background:linear-gradient(135deg,#2c2a27 0%,#5c5650 40%,#3e3a35 70%,#1f1d1b 100%)}
  .section .photo-challenges{background:linear-gradient(160deg,#3a3d32 0%,#57604f 35%,#8b938a 55%,#2e2c25 100%)}
  .section .bracket{position:absolute;left:16px;top:108px}
  .section .num-box{position:absolute;left:27px;top:119px;width:72px;height:72px;border:1.5px solid var(--accent-cyan);color:var(--white);font-size:56px;font-weight:700;display:flex;align-items:center;justify-content:center}
  .section h2{position:absolute;left:119px;top:127px;color:var(--white);font-weight:700;font-size:27px;line-height:32px;letter-spacing:.3px}

  /* Gift slides */
  .gift .band{position:absolute;left:0;right:0;top:101px;bottom:0;background:linear-gradient(180deg,var(--navy) 0%,var(--navy-deep) 100%)}
  .gift h3{position:absolute;top:11px;left:0;right:0;text-align:center;font-size:10px;font-weight:400;color:var(--ink);letter-spacing:.3px}
  .gift .category{position:absolute;top:28px;left:0;right:0;text-align:center;font-size:8px;color:var(--teal-link)}
  .gift .category::after{content:"";display:block;width:28px;height:1px;background:var(--teal-link);margin:4px auto 0}
  .gift-card{position:absolute;top:53px;width:90px;text-align:center}
  .gift-card .frame{width:90px;height:108px;background:var(--white);padding:4px;box-shadow:0 2px 5px rgba(0,0,0,.25)}
  .gift-card .frame div{width:100%;height:100%}
  .gift-card .price{width:64px;height:12px;border-radius:6px;background:var(--white);color:var(--price-red);font-size:7px;font-weight:700;line-height:12px;margin:12px auto 0}
  .gift-card .caption{color:var(--white);font-size:5.4px;line-height:7px;margin:6px -6px 0}
  .c1{left:28px}.c2{left:154px}.c3{left:282px}

  /* Solutions */
  .solve .photo{background:linear-gradient(180deg,#1f2a25 0%,#3a4538 45%,#27302a 100%)}
  .solve h3{position:absolute;top:21px;left:0;right:0;text-align:center;color:var(--white);font-size:10px;font-weight:700}
  .solve-box{position:absolute;top:53px;width:113px;height:140px;border:1.5px solid var(--accent-cyan);color:var(--white);text-align:center;font-size:7.5px;line-height:11px;padding:16px 8px 0}
  .solve-box svg{display:block;margin:0 auto 24px}
  .solve-box.highlight{background:var(--accent-cyan);border-color:var(--accent-cyan);top:59px;height:134px;width:106px}
  .s1{left:13px}.s2{left:145px}.s3{left:270px}
</style>
</head>
<body>
<main class="deck">

  <!-- Cover -->
  <section class="slide cover">
    <div class="photo" role="img" aria-label="Photo of a festival crowd throwing coloured powder"></div>
    <div class="brand-tab">
      <div class="brand-name">WAYFAREL<small>.gift</small></div>
      <div class="brand-tagline">专注精选体验式的礼品电商</div>
    </div>
    <div class="pitch-box">帮助企业一站式完美解决<br>员工个性化奖励<br>差异化客户礼品</div>
    <div class="footer">
      <div class="mark">FBV</div>
      <p class="disclaimer">This report is solely for the use of client personnel. No part of it may be circulated, quoted, or reproduced for distribution outside the client organization without prior written approval from Farbrookvale Company Limited.</p>
    </div>
  </section>

  <!-- Agenda -->
  <section class="slide agenda">
    <div class="photo" role="img" aria-label="Dusk city skyline with traditional rooftops"></div>
    <h2>AGENDA</h2>
    <div class="agenda-item" style="left:42px"><div class="num" style="background:var(--agenda-1)">1</div><p>Our Products</p></div>
    <div class="agenda-item" style="left:164px"><div class="num" style="background:var(--agenda-2)">2</div><p>Your Challenges</p></div>
    <div class="agenda-item" style="left:288px"><div class="num" style="background:var(--agenda-3)">3</div><p>How we can help?</p></div>
  </section>

  <!-- Section 1 -->
  <section class="slide section">
    <div class="photo photo-products" role="img" aria-label="Desk with a map, laptop and coffee seen from above"></div>
    <svg class="bracket" width="30" height="30" viewBox="0 0 30 30"><path d="M2 28V2h28" fill="none" stroke="var(--accent-cyan)" stroke-width="4"/></svg>
    <div class="num-box">1</div>
    <h2>OUR<br>PRODUCTS</h2>
  </section>

  <!-- Adventure -->
  <section class="slide gift">
    <div class="band"></div>
    <h3>WAYFAREL EXPERIENTIAL GIFTS</h3>
    <p class="category">Adventure</p>
    <div class="gift-card c1"><div class="frame"><div role="img" aria-label="Helicopter over mountains" style="background:linear-gradient(160deg,#c9a46a,#8a6a3c)"></div></div><div class="price">¥2000</div><p class="caption">Helicopter flight over the Great Wall.</p></div>
    <div class="gift-card c2"><div class="frame"><div role="img" aria-label="Climber on a sea cliff" style="background:linear-gradient(160deg,#6f9fc4,#2f5876)"></div></div><div class="price">¥328</div><p class="caption">Climb a sea cliff with expert guides.</p></div>
    <div class="gift-card c3"><div class="frame"><div role="img" aria-label="Red racing car on track" style="background:linear-gradient(160deg,#5a5a5a,#c8222a)"></div></div><div class="price">¥2322</div><p class="caption">Drive a race car for a day.</p></div>
  </section>

  <!-- Gourmet -->
  <section class="slide gift">
    <div class="band"></div>
    <h3>WAYFAREL EXPERIENTIAL GIFTS</h3>
    <p class="category">Gourmet</p>
    <div class="gift-card c1"><div class="frame"><div role="img" aria-label="Historic courtyard entrance" style="background:linear-gradient(180deg,#4c6a8a,#7a2a22)"></div></div><div class="price">¥1500</div><p class="caption">Private tea and dinner in a historic courtyard.</p></div>
    <div class="gift-card c2"><div class="frame"><div role="img" aria-label="Pot cooking over an open fire" style="background:linear-gradient(180deg,#6a5a44,#b0562a)"></div></div><div class="price">¥200</div><p class="caption">Cook a village hotpot over open fire.</p></div>
    <div class="gift-card c3"><div class="frame"><div role="img" aria-label="Chef preparing a dish" style="background:linear-gradient(180deg,#3a3a38,#6f6a5e)"></div></div><div class="price">¥328</div><p class="caption">Chef's table: cook with a private chef.</p></div>
  </section>

  <!-- Pampering -->
  <section class="slide gift">
    <div class="band"></div>
    <h3>WAYFAREL EXPERIENTIAL GIFTS</h3>
    <p class="category">Pampering</p>
    <div class="gift-card c1"><div class="frame"><div role="img" aria-label="Relaxing spa massage" style="background:linear-gradient(160deg,#c79a7a,#6e4a36)"></div></div><div class="price">¥720</div><p class="caption">A signature spa ritual, fully tailored.</p></div>
    <div class="gift-card c2"><div class="frame"><div role="img" aria-label="Partner yoga on an ancient wall" style="background:linear-gradient(180deg,#4f8fd0,#9aa6b0)"></div></div><div class="price">¥300</div><p class="caption">Partner yoga on the Great Wall.</p></div>
    <div class="gift-card c3"><div class="frame"><div role="img" aria-label="Tai chi silhouette at sunset" style="background:linear-gradient(180deg,#d8d2c4,#2a2622)"></div></div><div class="price">¥300</div><p class="caption">Tai chi lesson with a grand master.</p></div>
  </section>

  <!-- Culture -->
  <section class="slide gift">
    <div class="band"></div>
    <h3>WAYFAREL EXPERIENTIAL GIFTS</h3>
    <p class="category">Culture</p>
    <div class="gift-card c1"><div class="frame"><div role="img" aria-label="Palace tower at dusk by the moat" style="background:linear-gradient(180deg,#2d3a4a,#8a6a4a)"></div></div><div class="price">¥1000</div><p class="caption">After-hours palace tour with private guide.</p></div>
    <div class="gift-card c2"><div class="frame"><div role="img" aria-label="Hands making handmade paper" style="background:linear-gradient(160deg,#3a3430,#d8cfc0)"></div></div><div class="price">¥300</div><p class="caption">Paper making with a village artisan.</p></div>
    <div class="gift-card c3"><div class="frame"><div role="img" aria-label="Travellers with a horse in a village" style="background:linear-gradient(180deg,#8a8a84,#4a4a3e)"></div></div><div class="price">¥200</div><p class="caption">Ride with a Tibetan horse guide.</p></div>
  </section>

  <!-- Staycations -->
  <section class="slide gift">
    <div class="band"></div>
    <h3>WAYFAREL EXPERIENTIAL GIFTS</h3>
    <p class="category">Staycations</p>
    <div class="gift-card c1"><div class="frame"><div role="img" aria-label="Hotel room overlooking a harbour" style="background:linear-gradient(180deg,#9ab2bc,#4a5a60)"></div></div><div class="price">¥3960</div><p class="caption">Harbour hotel stay with afternoon tea.</p></div>
    <div class="gift-card c2"><div class="frame"><div role="img" aria-label="Mountain retreat lit at dusk" style="background:linear-gradient(180deg,#4a78b4,#2a3a30)"></div></div><div class="price">¥1950</div><p class="caption">Weekend retreat near the Great Wall.</p></div>
    <div class="gift-card c3"><div class="frame"><div role="img" aria-label="Theme park castle at night" style="background:linear-gradient(180deg,#1e2f7a,#6a4aa0)"></div></div><div class="price">¥5000</div><p class="caption">Family theme park trip with hotel stay.</p></div>
  </section>

  <!-- Section 2 -->
  <section class="slide section">
    <div class="photo photo-challenges" role="img" aria-label="Friends sitting by a waterfall"></div>
    <svg class="bracket" width="30" height="30" viewBox="0 0 30 30"><path d="M2 28V2h28" fill="none" stroke="var(--accent-cyan)" stroke-width="4"/></svg>
    <div class="num-box">2</div>
    <h2>YOUR<br>CHALLENGES</h2>
  </section>

  <!-- Solutions -->
  <section class="slide solve">
    <div class="photo" role="img" aria-label="Misty forest"></div>
    <h3>OUR EXPERIENTIAL GIFTS CAN HELP SOLVE</h3>
    <div class="solve-box s1">
      <svg width="48" height="44" viewBox="0 0 48 44" fill="none" stroke="#fff" stroke-width="2.5">
        <circle cx="12" cy="24" r="4" fill="#fff"/><path d="M5 40v-6a7 7 0 0 1 14 0v6z" fill="#fff"/>
        <circle cx="36" cy="24" r="4" fill="#fff"/><path d="M29 40v-6a7 7 0 0 1 14 0v6z" fill="#fff"/>
        <path d="M10 12a16 16 0 0 1 26-4"/><path d="M36 3v6h-6"/>
      </svg>
      More effectively engage and motivate customers and staff
    </div>
    <div class="solve-box s2 highlight">
      <svg width="54" height="46" viewBox="0 0 54 46" fill="#fff">
        <rect x="4" y="6" width="7" height="36"/><rect x="15" y="18" width="7" height="24"/><rect x="26" y="26" width="7" height="16"/><rect x="37" y="30" width="7" height="12"/>
        <path d="M6 4 Q22 30 44 26" fill="none" stroke="#fff" stroke-width="5"/><path d="M42 18l10 8-12 4z"/>
      </svg>
      Lowers overall cost
    </div>
    <div class="solve-box s3">
      <svg width="42" height="50" viewBox="0 0 42 50" fill="none" stroke="#fff" stroke-width="2.5">
        <circle cx="21" cy="18" r="15"/><circle cx="21" cy="18" r="9" fill="#fff"/>
        <path d="M12 30l-6 16 7-3 4 6 4-13M30 30l6 16-7-3-4 6-4-13"/>
      </svg>
      Create a recognition culture within the company
    </div>
  </section>

</main>
</body>
</html>
```